Modify an already created sticker/decal

I have product “Model Names” but I need this modified to a more universal “Horizontal in Orientation” so that it fits nicely on the product itself when printed as a sticker/decal. There will be (3) models to start with Trail Mule LX, Trail Mule SR, Trail Mule QVN model names. The branding needs to follow-through on all decals/stickers.

```html
<!DOCTYPE html>
<html lang="en">
<head>
<meta charset="utf-8">
<title>Trail Mule LX – Horizontal Decal</title>
<link rel="stylesheet" href="https://fonts.googleapis.com/css2?family=Krona+One&display=swap">
<style>
  :root {
    --canvas: #ffffff;
    --plate-dark: #000000;
    --plate-mid: #1c1c1c;
    --frame-light: #ebe9e8;
    --frame-mid: #c9c9c9;
    --frame-dark: #a7a7a7;
    --type-white: #ffffff;
    --accent-green: #8dd14a;
  }
  html, body {
    margin: 0;
    padding: 0;
    overflow: hidden;
    background: var(--canvas);
  }
  .decal-sheet {
    display: block;
    width: 1200px;
    height: 462px;
  }
  .model-name {
    font-family: "Krona One", "Arial Black", sans-serif;
    font-size: 76px;
    fill: var(--type-white);
  }
  .model-accent { fill: var(--accent-green); }
</style>
</head>
<body>
<svg class="decal-sheet" viewBox="0 0 1200 462" xmlns="http://www.w3.org/2000/svg">
  <defs>
    <linearGradient id="frameSilver" x1="0" y1="0" x2="1" y2="0.3">
      <stop offset="0" stop-color="var(--frame-light)"/>
      <stop offset="0.45" stop-color="var(--frame-light)"/>
      <stop offset="0.7" stop-color="var(--frame-mid)"/>
      <stop offset="0.9" stop-color="var(--frame-dark)"/>
      <stop offset="1" stop-color="var(--frame-mid)"/>
    </linearGradient>
    <radialGradient id="plateTone" cx="0.5" cy="0.5" r="0.7">
      <stop offset="0" stop-color="var(--plate-mid)"/>
      <stop offset="1" stop-color="var(--plate-dark)"/>
    </radialGradient>
  </defs>

  <!-- Framed decal variant -->
  <g class="decal decal--framed">
    <rect class="decal-frame" x="91" y="102" width="1018" height="116" fill="url(#frameSilver)"/>
    <rect class="decal-plate" x="104" y="114" width="993" height="91" fill="url(#plateTone)"
          role="img" aria-label="Black diamond-plate metal texture background"/>
    <rect class="model-accent" x="124" y="146" width="26" height="26"/>
    <text class="model-name" x="170" y="188" textLength="900" lengthAdjust="spacingAndGlyphs">TRAIL MULE LX</text>
  </g>

  <!-- Unframed decal variant -->
  <g class="decal decal--plain">
    <rect class="decal-plate" x="101" y="260" width="998" height="103" fill="url(#plateTone)"
          role="img" aria-label="Black diamond-plate metal texture background"/>
    <rect class="model-accent" x="124" y="298" width="26" height="26"/>
    <text class="model-name" x="170" y="339" textLength="900" lengthAdjust="spacingAndGlyphs">TRAIL MULE LX</text>
  </g>
</svg>
</body>
</html>
```